cookie box packaging sleeve design

Hi,
I'm looking to create 5 sleeves for cookies in a box.
Classic look, not too many colors. I need to be able to add the nutrition info for each sleeve at the back.
width 110 mm height 370mm

1. Salted Tahini Choc-Chip Cookie
2. Brownie White Choc Cookie
3. Peanut Butter Cookie
4. Earthquake Cookie
5.Pistachio Cookie

ideas:
Biscotti by Brellanti (https://ryde.brellanti.example/?welcomed)
OR
https://au.snapvorra.example/pin/4830195726104388/

Target Market(s)

Family, office and for gifts

Industry/Entity Type

Cafe/Bakery

Colors

Designer to choose colors to be used in the design.

Requirements
Should not have
• Too many colours and the photo of the cookies

```html
<!DOCTYPE html>
<html lang="en">
<head>
<meta charset="utf-8">
<title>Torvina House – Cookie Sleeves</title>
<link rel="stylesheet" href="https://fonts.googleapis.com/css2?family=Archivo+Black&family=Chewy&family=Roboto+Condensed:wght@400;700&display=swap">
<style>
  :root {
    --page: #ffffff;
    --ink: #111111;
    --panel: #ffffff;
    --pistachio-bg: #b8d27c;
    --pistachio-blob: #5b7320;
    --brownie-bg: #df720f;
    --brownie-blob: #5a2608;
    --peanut-bg: #fde600;
    --peanut-blob: #7b4d08;
    --quake-bg: #c3c4c1;
    --quake-blob: #3b1f17;
    --tahini-bg: #8dd0e7;
    --tahini-blob: #46599e;
  }
  * { box-sizing: border-box; margin: 0; padding: 0; }
  html, body { width: 1200px; height: 1200px; overflow: hidden; background: var(--page); }
  .sleeve-row { position: relative; width: 1200px; height: 1200px; }
  .sleeve {
    position: absolute; top: 296px; width: 188px; height: 633px;
    background: var(--bg); overflow: hidden;
  }
  .sleeve--pistachio { left: 51px;  --bg: var(--pistachio-bg); --blob: var(--pistachio-blob); }
  .sleeve--brownie   { left: 286px; --bg: var(--brownie-bg);   --blob: var(--brownie-blob); }
  .sleeve--peanut    { left: 513px; --bg: var(--peanut-bg);    --blob: var(--peanut-blob); }
  .sleeve--quake     { left: 741px; --bg: var(--quake-bg);     --blob: var(--quake-blob); }
  .sleeve--tahini    { left: 971px; --bg: var(--tahini-bg);    --blob: var(--tahini-blob); }

  .nutrition-tab {
    position: absolute; top: 28px; left: 61px; width: 67px; height: 32px;
    background: var(--panel); border-radius: 12px 12px 0 0;
    font-family: "Archivo Black", sans-serif; font-size: 17px; text-align: center;
    line-height: 34px; color: var(--ink);
  }
  .nutrition-panel {
    position: absolute; top: 48px; left: 21px; width: 146px; height: 168px;
    background: var(--panel); border-radius: 14px; padding: 10px 14px 0;
    color: var(--ink); font-family: "Roboto Condensed", sans-serif;
  }
  .nutrition-title {
    font-family: "Archivo Black", sans-serif; font-size: 11.4px; text-align: center;
    letter-spacing: 0.1px; white-space: nowrap; line-height: 14px;
  }
  .nutrition-rule { height: 4px; background: var(--ink); margin-top: 5px; }
  .nutrition-row {
    display: flex; justify-content: space-between; font-size: 8px; line-height: 14px;
    border-bottom: 1px solid var(--ink);
  }
  .nutrition-row--plain { border-bottom: 0; margin-top: 2px; }
  .nutrition-row--daily { justify-content: flex-end; border-bottom: 2px solid var(--ink); margin-top: 2px; }
  .nutrition-row--bold { font-weight: 700; }
  .nutrition-ingredients { font-size: 4.6px; line-height: 6px; margin-top: 6px; }

  .brand {
    position: absolute; top: 256px; left: 0; width: 100%; text-align: center;
    font-family: "Roboto Condensed", sans-serif; font-weight: 700; color: var(--ink);
  }
  .brand-name { font-size: 40px; line-height: 42px; letter-spacing: -0.5px; }
  .brand-sub { font-size: 11px; letter-spacing: 4px; line-height: 14px; }

  .flavour-splash {
    position: absolute; top: 330px; left: 16px; width: 156px; height: 112px;
    background: var(--blob); border-radius: 38px 46px 34px 50px / 40px 34px 46px 36px;
    display: flex; flex-direction: column; justify-content: center; align-items: center;
    color: #ffffff; text-align: center;
  }
  .flavour-name { font-family: "Chewy", cursive; font-size: 23px; line-height: 24px; letter-spacing: 0.5px; }
  .flavour-kind { font-family: "Roboto Condensed", sans-serif; font-weight: 700; font-size: 16px; line-height: 18px; }

  .cookie-photo {
    position: absolute; top: 454px; left: 0; width: 188px; height: 179px;
    border-radius: 60px 60px 0 0 / 16px 16px 0 0;
  }
  .sleeve--pistachio .cookie-photo { background: radial-gradient(circle at 45% 55%, #a7a14b, #8f6b2e 60%, #7b5424); }
  .sleeve--brownie .cookie-photo   { background: radial-gradient(circle at 50% 50%, #5a3524, #3e2318 65%, #2e1912); }
  .sleeve--peanut .cookie-photo    { background: radial-gradient(circle at 50% 50%, #e9cb90, #d6b273 65%, #c79f5f); }
  .sleeve--quake .cookie-photo     { background: radial-gradient(circle at 55% 40%, #f4f2f2, #d9d3d3 45%, #5a2e26 80%); }
  .sleeve--tahini .cookie-photo    { background: radial-gradient(circle at 50% 55%, #d9b56f, #c79e5a 60%, #b48848); }

  .net-weight {
    position: absolute; top: 578px; left: 136px; width: 44px; height: 44px; border-radius: 50%;
    background: var(--ink); border: 1.5px solid #ffffff; outline: 2px solid var(--ink);
    color: #ffffff; font-family: "Roboto Condensed", sans-serif; font-size: 8px; line-height: 9px;
    display: flex; flex-direction: column; justify-content: center; align-items: center;
  }
</style>
</head>
<body>
<main class="sleeve-row">

  <section class="sleeve sleeve--pistachio">
    <div class="nutrition-tab">MY</div>
    <div class="nutrition-panel">
      <p class="nutrition-title">NUTRITION FACTS</p>
      <div class="nutrition-rule"></div>
      <p class="nutrition-row nutrition-row--plain"><span>SERVING SIZE:</span><span>XXX</span></p>
      <p class="nutrition-row nutrition-row--daily"><span>%DAILY VALUE**</span></p>
      <p class="nutrition-row nutrition-row--bold"><span>LOREM IPSUM:</span><span>XXX</span></p>
      <p class="nutrition-row"><span>LOREM IPSUM:</span><span>XXX</span></p>
      <p class="nutrition-row"><span>LOREM IPSUM:</span><span>XXX</span></p>
      <p class="nutrition-row"><span>LOREM IPSUM:</span><span>XXX</span></p>
      <p class="nutrition-ingredients">Ingredients: Lorem ipsum dolor sit amet, consectetur adipiscing elit, sed do eiusmod tempor incididunt ut labore.</p>
    </div>
    <div class="brand"><p class="brand-name">Torvina</p><p class="brand-sub">HOUSE</p></div>
    <div class="flavour-splash"><p class="flavour-name">Pistachio</p><p class="flavour-kind">cookie</p></div>
    <div class="cookie-photo" role="img" aria-label="Close-up photo of a pistachio cookie topped with chopped pistachios"></div>
    <div class="net-weight"><span>Net WT</span><span>280g</span></div>
  </section>

  <section class="sleeve sleeve--brownie">
    <div class="nutrition-tab">MY</div>
    <div class="nutrition-panel">
      <p class="nutrition-title">NUTRITION FACTS</p>
      <div class="nutrition-rule"></div>
      <p class="nutrition-row nutrition-row--plain"><span>SERVING SIZE:</span><span>XXX</span></p>
      <p class="nutrition-row nutrition-row--daily"><span>%DAILY VALUE**</span></p>
      <p class="nutrition-row nutrition-row--bold"><span>LOREM IPSUM:</span><span>XXX</span></p>
      <p class="nutrition-row"><span>LOREM IPSUM:</span><span>XXX</span></p>
      <p class="nutrition-row"><span>LOREM IPSUM:</span><span>XXX</span></p>
      <p class="nutrition-row"><span>LOREM IPSUM:</span><span>XXX</span></p>
      <p class="nutrition-ingredients">Ingredients: Lorem ipsum dolor sit amet, consectetur adipiscing elit, sed do eiusmod tempor incididunt ut labore.</p>
    </div>
    <div class="brand"><p class="brand-name">Torvina</p><p class="brand-sub">HOUSE</p></div>
    <div class="flavour-splash"><p class="flavour-name">Brownie<br>White</p><p class="flavour-kind">cookie</p></div>
    <div class="cookie-photo" role="img" aria-label="Close-up photo of a brownie white chocolate cookie with sea salt flakes"></div>
    <div class="net-weight"><span>Net WT</span><span>280g</span></div>
  </section>

  <section class="sleeve sleeve--peanut">
    <div class="nutrition-tab">MY</div>
    <div class="nutrition-panel">
      <p class="nutrition-title">NUTRITION FACTS</p>
      <div class="nutrition-rule"></div>
      <p class="nutrition-row nutrition-row--plain"><span>SERVING SIZE:</span><span>XXX</span></p>
      <p class="nutrition-row nutrition-row--daily"><span>%DAILY VALUE**</span></p>
      <p class="nutrition-row nutrition-row--bold"><span>LOREM IPSUM:</span><span>XXX</span></p>
      <p class="nutrition-row"><span>LOREM IPSUM:</span><span>XXX</span></p>
      <p class="nutrition-row"><span>LOREM IPSUM:</span><span>XXX</span></p>
      <p class="nutrition-row"><span>LOREM IPSUM:</span><span>XXX</span></p>
      <p class="nutrition-ingredients">Ingredients: Lorem ipsum dolor sit amet, consectetur adipiscing elit, sed do eiusmod tempor incididunt ut labore.</p>
    </div>
    <div class="brand"><p class="brand-name">Torvina</p><p class="brand-sub">HOUSE</p></div>
    <div class="flavour-splash"><p class="flavour-name">Peanut<br>Butter</p><p class="flavour-kind">cookie</p></div>
    <div class="cookie-photo" role="img" aria-label="Close-up photo of a peanut butter cookie topped with chopped peanuts"></div>
    <div class="net-weight"><span>Net WT</span><span>280g</span></div>
  </section>

  <section class="sleeve sleeve--quake">
    <div class="nutrition-tab">MY</div>
    <div class="nutrition-panel">
      <p class="nutrition-title">NUTRITION FACTS</p>
      <div class="nutrition-rule"></div>
      <p class="nutrition-row nutrition-row--plain"><span>SERVING SIZE:</span><span>XXX</span></p>
      <p class="nutrition-row nutrition-row--daily"><span>%DAILY VALUE**</span></p>
      <p class="nutrition-row nutrition-row--bold"><span>LOREM IPSUM:</span><span>XXX</span></p>
      <p class="nutrition-row"><span>LOREM IPSUM:</span><span>XXX</span></p>
      <p class="nutrition-row"><span>LOREM IPSUM:</span><span>XXX</span></p>
      <p class="nutrition-row"><span>LOREM IPSUM:</span><span>XXX</span></p>
      <p class="nutrition-ingredients">Ingredients: Lorem ipsum dolor sit amet, consectetur adipiscing elit, sed do eiusmod tempor incididunt ut labore.</p>
    </div>
    <div class="brand"><p class="brand-name">Torvina</p><p class="brand-sub">HOUSE</p></div>
    <div class="flavour-splash"><p class="flavour-name">Earth<br>Quake</p><p class="flavour-kind">cookie</p></div>
    <div class="cookie-photo" role="img" aria-label="Close-up photo of a chocolate crinkle earthquake cookie dusted with icing sugar"></div>
    <div class="net-weight"><span>Net WT</span><span>280g</span></div>
  </section>

  <section class="sleeve sleeve--tahini">
    <div class="nutrition-tab">MY</div>
    <div class="nutrition-panel">
      <p class="nutrition-title">NUTRITION FACTS</p>
      <div class="nutrition-rule"></div>
      <p class="nutrition-row nutrition-row--plain"><span>SERVING SIZE:</span><span>XXX</span></p>
      <p class="nutrition-row nutrition-row--daily"><span>%DAILY VALUE**</span></p>
      <p class="nutrition-row nutrition-row--bold"><span>LOREM IPSUM:</span><span>XXX</span></p>
      <p class="nutrition-row"><span>LOREM IPSUM:</span><span>XXX</span></p>
      <p class="nutrition-row"><span>LOREM IPSUM:</span><span>XXX</span></p>
      <p class="nutrition-row"><span>LOREM IPSUM:</span><span>XXX</span></p>
      <p class="nutrition-ingredients">Ingredients: Lorem ipsum dolor sit amet, consectetur adipiscing elit, sed do eiusmod tempor incididunt ut labore.</p>
    </div>
    <div class="brand"><p class="brand-name">Torvina</p><p class="brand-sub">HOUSE</p></div>
    <div class="flavour-splash"><p class="flavour-name">Salted<br>Tahini</p><p class="flavour-kind">cookie</p></div>
    <div class="cookie-photo" role="img" aria-label="Close-up photo of a salted tahini cookie with chocolate chunks"></div>
    <div class="net-weight"><span>Net WT</span><span>280g</span></div>
  </section>

</main>
</body>
</html>
```